Namecard Designs+Logo for a High End Automobile Company

We need a new business card for our company called Velta Motorhof.

www.veltamotorhof.example.sg
Our new website will be up in 2.5 months time.

We sell used and brand new continental cars like Korvane, QTL, Dravell, Solbrini and etc. Currently we are operating from 2 offices in Singapore and United Kingdom.

We want a design which is serious. We are open to colours but try to keep it at a maximum of 3 colours.

We prefer something simple and minimal. We are open to 2 sides printing or even 2 sided namecards. Both UK and Singapore company offices address must be in; either side by side, front and back, or even 2 sided cards.

The logo can be a text logo, emblem, abstract, pictorial or combination.

We are printing with Pribo.com so please kindly follow the printing guideline.

http://uk.pribo.example/help/faq/templates-and-guidelines.html

Rich and Car Enthusiasts

Printing

Must have
• Our 2 offices; UK and Singapore.

Our slogan which is " The Automobile Specialist"
Should not have
• Not more than 3 colours

```html
<!DOCTYPE html>
<html lang="en">
<head>
<meta charset="utf-8">
<title>Velta Motorhof – Business Cards</title>
<link rel="stylesheet" href="https://fonts.googleapis.com/css2?family=PT+Sans:wght@400;700&display=swap">
<style>
  :root {
    --page: #ffffff;
    --label: #333333;
    --card-light: #f4f4f4;
    --card-mid: #c9c9c9;
    --band-dark: #1e1c1a;
    --band-mid: #34312e;
    --band-soft: #47433f;
    --logo-grey: #5a5a5a;
    --ink: #222222;
    --ink-soft: #444444;
  }
  * { box-sizing: border-box; margin: 0; padding: 0; }
  html, body {
    width: 1200px; height: 900px; overflow: hidden;
    background: var(--page);
    font-family: "PT Sans", Arial, sans-serif;
  }
  .sheet { position: relative; width: 1200px; height: 900px; }

  .sheet-label {
    position: absolute;
    font-size: 19px;
    color: var(--label);
    text-align: center;
    width: 500px;
  }

  .card {
    position: absolute;
    overflow: hidden;
    background: radial-gradient(ellipse at 50% 45%, var(--card-light) 0%, #e2e2e2 50%, var(--card-mid) 100%);
    box-shadow: 4px 6px 10px rgba(0,0,0,0.35);
  }
  .card-front { width: 496px; height: 284px; top: 160px; }
  .card-front--one { left: 80px; }
  .card-front--two { left: 622px; }
  .card-back { width: 510px; height: 286px; left: 350px; top: 550px; }

  .card-bands { position: absolute; inset: 0; width: 100%; height: 100%; }

  .brand {
    position: absolute; left: 0; right: 0; top: 86px;
    text-align: center;
  }
  .brand-name {
    font-weight: 700;
    font-size: 52px;
    line-height: 1;
    color: var(--logo-grey);
    letter-spacing: -0.5px;
  }
  .brand-slogan {
    margin-top: 4px;
    font-size: 13px;
    line-height: 16px;
    font-weight: 400;
    letter-spacing: 4.4px;
    color: var(--ink);
    text-transform: uppercase;
  }
  .brand--with-mark { top: 90px; }
  .brand--with-mark .brand-row {
    display: flex; align-items: center; justify-content: center; gap: 8px;
  }
  .brand--with-mark .brand-name { font-size: 50px; }
  .brand-mark {
    width: 46px; height: 46px; border-radius: 50%;
    background: var(--logo-grey);
  }
  .brand--with-mark .brand-slogan { padding-left: 54px; }

  .holder { position: absolute; left: 34px; top: 36px; color: var(--ink); }
  .holder-name { font-size: 16px; font-weight: 700; line-height: 1.1; }
  .holder-title { font-size: 11px; line-height: 1.2; }

  .contact-list {
    position: absolute; left: 34px; top: 90px;
    list-style: none; font-size: 10.5px; color: var(--ink-soft); line-height: 16px;
  }
  .contact-key {
    display: inline-block; width: 12px; font-weight: 700; color: var(--ink);
    border-right: 1px solid var(--ink-soft); margin-right: 6px;
  }
  .contact-web { font-weight: 700; color: var(--ink); margin-top: 2px; }

  .offices {
    position: absolute; right: 30px; top: 90px;
    text-align: right; font-size: 10.5px; line-height: 14px; color: var(--ink-soft);
  }
  .office + .office { margin-top: 10px; }
  .office-city { font-weight: 700; color: var(--ink); text-transform: uppercase; }
</style>
</head>
<body>
<main class="sheet">

  <svg width="0" height="0" style="position:absolute" aria-hidden="true">
    <defs>
      <linearGradient id="band-shade" x1="0" y1="0" x2="1" y2="0">
        <stop offset="0" stop-color="#2b2826"/>
        <stop offset="0.5" stop-color="#1b1917"/>
        <stop offset="1" stop-color="#2b2826"/>
      </linearGradient>
      <linearGradient id="edge-shine" x1="0" y1="0" x2="1" y2="0">
        <stop offset="0" stop-color="#9a9a9a"/>
        <stop offset="0.45" stop-color="#ffffff"/>
        <stop offset="1" stop-color="#a8a8a8"/>
      </linearGradient>
    </defs>
  </svg>

  <p class="sheet-label" style="left:78px;top:110px;">Business card_Front_Option 1</p>
  <p class="sheet-label" style="left:620px;top:110px;">Business card_Front_Option 2</p>

  <section class="card card-front card-front--one">
    <svg class="card-bands" viewBox="0 0 496 284" preserveAspectRatio="none" aria-hidden="true">
      <path d="M0,0 H496 V12 Q250,20 0,62 Z" fill="url(#band-shade)"/>
      <path d="M0,0 H496 V4 Q260,10 0,38 Z" fill="var(--band-mid)" opacity="0.7"/>
      <path d="M0,62 Q250,20 496,12" fill="none" stroke="url(#edge-shine)" stroke-width="3"/>
      <path d="M0,284 V222 Q250,168 496,180 V284 Z" fill="url(#band-shade)"/>
      <path d="M0,284 V248 Q250,196 496,206 V284 Z" fill="var(--band-mid)" opacity="0.75"/>
      <path d="M60,284 Q260,226 496,238 V284 Z" fill="var(--band-soft)" opacity="0.45"/>
      <path d="M0,222 Q250,168 496,180" fill="none" stroke="url(#edge-shine)" stroke-width="3"/>
    </svg>
    <div class="brand">
      <p class="brand-name">Velta Motorhof</p>
      <p class="brand-slogan">European Automobile Specialist</p>
    </div>
  </section>

  <section class="card card-front card-front--two">
    <svg class="card-bands" viewBox="0 0 496 284" preserveAspectRatio="none" aria-hidden="true">
      <path d="M0,284 V220 Q240,164 496,178 V284 Z" fill="url(#band-shade)"/>
      <path d="M0,284 V246 Q240,194 496,206 V284 Z" fill="var(--band-mid)" opacity="0.75"/>
      <path d="M60,284 Q260,226 496,240 V284 Z" fill="var(--band-soft)" opacity="0.45"/>
      <path d="M0,220 Q240,164 496,178" fill="none" stroke="url(#edge-shine)" stroke-width="3"/>
    </svg>
    <div class="brand brand--with-mark">
      <div class="brand-row">
        <span class="brand-mark"></span>
        <p class="brand-name">Velta Motorhof</p>
      </div>
      <p class="brand-slogan">European Automobile Specialist</p>
    </div>
  </section>

  <p class="sheet-label" style="left:355px;top:506px;">Business card_Back</p>

  <section class="card card-back">
    <svg class="card-bands" viewBox="0 0 510 286" preserveAspectRatio="none" aria-hidden="true">
      <path d="M0,286 V250 Q240,176 510,196 V286 Z" fill="url(#band-shade)"/>
      <path d="M0,286 V270 Q250,208 510,224 V286 Z" fill="var(--band-mid)" opacity="0.75"/>
      <path d="M80,286 Q280,240 510,252 V286 Z" fill="var(--band-soft)" opacity="0.45"/>
      <path d="M0,250 Q240,176 510,196" fill="none" stroke="url(#edge-shine)" stroke-width="3"/>
    </svg>

    <div class="holder">
      <p class="holder-name">MR. KD Arlen</p>
      <p class="holder-title">Sales Director</p>
    </div>

    <ul class="contact-list">
      <li><span class="contact-key">C</span>+44 (0) 98 765 4320</li>
      <li><span class="contact-key">T</span>+44 (0) 98 765 4320</li>
      <li><span class="contact-key">F</span>+44 (0) 98 765 4320</li>
      <li><span class="contact-key">E</span>kian@veltamotorhof.example</li>
      <li class="contact-web">www.veltamotorhof.example.sg</li>
    </ul>

    <div class="offices">
      <div class="office">
        <p class="office-city">Europe</p>
        <p>14 Harwell Lane</p>
        <p>London</p>
      </div>
      <div class="office">
        <p class="office-city">Singapore</p>
        <p>8 Keppel Walk</p>
        <p>Singapore</p>
      </div>
    </div>
  </section>

</main>
</body>
</html>
```